Design a Website in Wordpress for an Australian Health Training Company in Health related courses

We require a WORDPRESS based Website (due to add on's we need to use for third party software) to replace our old site.
We offer national face to face delivery in medical reception, terminology and also administration.
The website will have around 6 pages and the ability to describe our main 6 courses (perhaps on the Courses page this may be tabs opening up to details for example?)
I have attached a previous sample of a Joomla site which was being developed (please do not feel you have to copy this - but I am just giving it as a sample - copying would be boring). But it gives an idea of look/feel and colours which may be suitable. Open to other ideas though.
I will provide some of the content, but would like the ability to finish the content myself.
Images and graphics are important. While a few medical photos re great - don't be tempted to us all pictures of doctors and nurses (although a couple would be good) - these are administrative courses so general corporate, eye catching visionary pictures of people in general are great. A medical type picture is also fine.
THE BOOKING system - will be via an ADD ON which will occur at the end of the project and is supplied by a third party software company (our student management system). This project will include up to 2 hours working with the Tech guys from the third party software to enable the ADD ON. If this ADD ON requires more time, we will pay hourly (although I do not expect it will).
Mostly a female market, many mature aged women target 25-45 yrs. Mixture of medical/health and corporate. Maybe a bit of mums returning to work and corporate inspiration.
Must have
- Wordpress
- Great graphics
- Interesting
- professional and clean
- Enquiry section (info Pak)
- Should have a University feel to it - Education
- Pages
- Home Page - About Us - Recruitment -Courses - Class Schedule - Traineeships Queensland Funding - Latest News Blog - Corporate Training- Contact us

```html
<!DOCTYPE html>
<html lang="en">
<head>
<meta charset="utf-8">
<title>Harlow – Courses for Busy People</title>
<link rel="stylesheet" href="https://fonts.googleapis.com/css2?family=Roboto:ital,wght@0,300;0,400;0,500;0,700;1,400&family=Great+Vibes&display=swap">
<style>
:root{
  --blue:#1a4fa3;
  --blue-deep:#134491;
  --ink:#222831;
  --text:#555b63;
  --muted:#8b9097;
  --line:#c9ced6;
  --panel:#e9eaec;
  --band:#f1f2f4;
  --footer:#2f343b;
  --footer-text:#9aa0a8;
  --white:#ffffff;
}
*{box-sizing:border-box;margin:0;padding:0}
html,body{width:1200px;height:3279px;overflow:hidden}
body{font-family:"Roboto",Arial,sans-serif;color:var(--text);background:var(--white);font-size:13px}
a{color:inherit;text-decoration:none}

/* top bar */
.topbar{height:30px;display:flex;align-items:center;justify-content:space-between;padding:0 52px;font-size:11.5px;color:var(--muted);border-bottom:1px solid #eceef1}
.topbar nav{display:flex;gap:26px}
.topbar .util{display:flex;gap:22px;align-items:center}
.flag{display:inline-block;width:16px;height:10px;vertical-align:middle;margin-right:5px;background:#1b3d8f;box-shadow:inset 0 0 0 2px #fff, inset 0 0 0 3px #c8262d}

/* header */
.header{height:68px;display:flex;align-items:center;justify-content:space-between;padding:0 52px 0 66px}
.brand{display:flex;align-items:center;gap:8px;font-weight:700;font-size:20px;color:var(--blue-deep)}
.brand .mark{width:14px;height:14px;background:var(--blue-deep)}
.mainnav{display:flex;gap:34px;font-size:13.5px;color:var(--ink)}

/* hero */
.hero{position:relative;height:558px;overflow:hidden}
.hero .photo{position:absolute;inset:0;background:linear-gradient(160deg,#c7a98a 0%,#8f7866 30%,#6b6a6f 55%,#a7a9ad 80%,#d8cdbf 100%)}
.hero .shade{position:absolute;inset:0;background:rgba(20,22,28,.35)}
.hero .inner{position:relative;text-align:center;color:var(--white);padding-top:158px}
.hero h1{font-family:"Great Vibes",cursive;font-weight:400;font-size:90px;letter-spacing:4px;line-height:1}
.hero p{font-size:22px;line-height:33px;margin:16px auto 0;width:760px;font-weight:400}
.hero .actions{display:flex;justify-content:center;gap:50px;margin-top:22px}
.btn{display:inline-block;font-size:10.5px;font-weight:500;letter-spacing:.5px;padding:11px 15px;text-transform:uppercase}
.btn-light{background:var(--white);color:var(--blue)}
.btn-ghost{border:1px solid var(--white);color:var(--white)}
.dots{position:absolute;left:0;right:0;top:518px;display:flex;justify-content:center;gap:8px}
.dots i{width:9px;height:9px;border-radius:50%;border:1.5px solid #fff}
.dots i.on{background:#fff}

/* section heads */
.sec-title{text-align:center;color:var(--blue);font-size:20px;font-weight:500}
.sec-title::after{content:"";display:block;margin:12px auto 0;width:1100px;border-bottom:2px dotted var(--line)}

/* intro */
.intro{height:387px;padding-top:13px}
.intro .copy{width:1050px;margin:48px auto 0;text-align:center;font-size:12.5px;line-height:20px}
.intro .copy p{margin-bottom:17px}

/* courses */
.courses{height:290px;background:var(--band);padding-top:12px}
.course-list{display:flex;gap:30px;padding-left:44px;margin-top:40px}
.course{width:162px;height:179px;background:var(--panel);position:relative;text-align:center;padding-top:72px;margin-top:50px}
.course .ico{position:absolute;top:-50px;left:33px;width:96px;height:96px;border-radius:50%;background:var(--blue);border:5px solid #fff;box-shadow:0 0 0 1px #d5d8dd;display:flex;align-items:center;justify-content:center}
.course h3{font-size:16px;font-weight:500;color:var(--ink);line-height:23px;padding:0 8px}

/* enrol band */
.enrol{margin-top:11px;height:164px;background:var(--blue);display:flex;align-items:center;justify-content:space-between;padding:0 78px 0 52px}
.enrol h2{color:var(--white);font-weight:400;font-size:28px;line-height:40px}
.enrol .btn{background:var(--white);color:var(--blue);font-size:12px;padding:14px 20px;font-weight:700}

/* values */
.values{position:relative;height:389px;overflow:hidden}
.values .photo{position:absolute;inset:0;background:linear-gradient(180deg,#3c4450 0%,#6a727d 45%,#4a525d 100%)}
.values .shade{position:absolute;inset:0;background:rgba(15,18,24,.45)}
.value-list{position:relative;display:flex;padding:54px 0 0 44px;gap:24px}
.value{width:210px;text-align:center;color:#eef0f3}
.value .ico{width:90px;height:90px;border-radius:50%;background:var(--blue);margin:0 auto;display:flex;align-items:center;justify-content:center}
.value.active .ico{background:transparent;border:3px solid #fff}
.value.active .ico span{width:64px;height:64px;border-radius:50%;background:var(--blue);display:flex;align-items:center;justify-content:center}
.value h3{font-size:17px;font-weight:500;margin-top:36px;color:var(--white)}
.value.active h3{color:#7fa6e0}
.value p{font-size:11.5px;line-height:17px;margin-top:18px;padding:0 6px}

/* testimonials */
.reviews{height:433px;padding-top:21px}
.review-grid{position:relative;width:1100px;margin:40px auto 0;display:grid;grid-template-columns:1fr 1fr}
.review-grid::before{content:"";position:absolute;left:50%;top:0;bottom:0;border-left:2px dotted var(--line)}
.review{display:flex;gap:24px;padding:6px 28px 20px 54px;align-items:flex-start}
.review.right{padding:6px 20px 20px 30px}
.review.row2{border-top:2px dotted var(--line);padding-top:30px}
.review blockquote{font-style:italic;font-size:11.5px;line-height:18px;flex:1}
.review.left blockquote{text-align:right}
.review cite{display:block;font-style:normal;font-size:11px;color:var(--ink);margin-top:14px}
.avatar{width:76px;height:76px;border-radius:50%;flex:none;border:3px solid #eee}

/* posts */
.posts{height:551px;padding-top:20px;text-align:center}
.post-list{display:flex;gap:30px;padding-left:52px;margin-top:53px;text-align:left}
.post{width:252px;height:362px;background:#f4f5f6}
.post .thumb{height:192px;position:relative}
.post .body{padding:14px 17px 0}
.post h3{font-size:16px;font-weight:500;color:var(--ink)}
.post p{font-size:12.5px;line-height:18px;margin-top:10px;height:72px}
.post .meta{display:flex;justify-content:space-between;border-top:1px solid #dde0e4;padding-top:12px;margin-top:12px;font-size:10.5px;color:var(--muted)}
.more{display:inline-block;margin-top:36px;background:var(--blue);color:#fff;font-size:11px;font-weight:700;padding:11px 19px}

/* footer */
.footer{height:398px;background:var(--footer);color:var(--footer-text);position:relative;padding-top:32px}
.cols{display:flex;padding-left:52px}
.col{width:282px;padding-right:40px}
.col h4{color:#e6e8eb;font-size:16px;font-weight:500;margin-bottom:24px}
.col p{font-size:11.5px;line-height:17px}
.social{display:flex;gap:10px;margin-top:14px}
.social i{width:11px;height:11px;border-radius:50%;background:var(--footer-text)}
.mini{display:flex;gap:14px;align-items:center;margin-bottom:20px}
.mini .dot{width:36px;height:36px;border-radius:50%;background:#9a9ea5;flex:none}
.mini b{display:block;color:#e6e8eb;font-weight:400;font-size:11.5px}
.mini small{font-size:10px}
.contact p{margin-bottom:12px}
.contact strong{color:#e6e8eb;font-weight:400}
.copyright{position:absolute;left:52px;right:52px;bottom:0;border-top:1px solid #444a52;height:55px;display:flex;align-items:center;font-size:11px}
</style>
</head>
<body>

<div class="topbar">
  <nav><a href="#">Home</a><a href="#">About Us</a><a href="#">Blog</a><a href="#">Contact us</a></nav>
  <div class="util"><span><span class="flag"></span>English ▾</span><span>Login/Register</span>
    <svg width="12" height="12" viewBox="0 0 12 12"><circle cx="5" cy="5" r="3.8" fill="none" stroke="#8b9097" stroke-width="1.6"/><line x1="8" y1="8" x2="11" y2="11" stroke="#8b9097" stroke-width="1.6"/></svg></div>
</div>

<header class="header">
  <div class="brand"><span class="mark"></span>Harlow</div>
  <nav class="mainnav"><a href="#">Recruitment</a><a href="#">Courses</a><a href="#">Class Schedule</a><a href="#">Traineeships Queensland</a><a href="#">Funding</a><a href="#">Corporate Training</a></nav>
</header>

<section class="hero">
  <div class="photo" role="img" aria-label="Photo of adult learners studying together in a bright classroom"></div>
  <div class="shade"></div>
  <div class="inner">
    <h1>Courses for Busy People</h1>
    <p>Our unique swiftSTEP(Combined Assesment &amp; Training) class format delivers accelerated training that's specifically targeted at busy profes-sionals</p>
    <div class="actions"><a class="btn btn-light" href="#">Read more</a><a class="btn btn-ghost" href="#">Go on surfing</a></div>
  </div>
  <div class="dots"><i class="on"></i><i></i><i class="on"></i></div>
</section>

<section class="intro">
  <h2 class="sec-title">Intro</h2>
  <div class="copy">
    <p>Harlow is Australia's Leading Provider of Educational, Training and Support Services for the Medical and Dental industry - enabling students to be immediately skilled and 'Job Ready' for a career in Health.</p>
    <p>Harlow is a Registered Training Organisation offering specialised Medical Administration Training in over 15 locations Australia wide. Harlow have trained thousands of students the required knowledge and skills to become successful health care administrators.</p>
    <p>Our unique Short Medical Reception and Terminology Course and our Full Qualification is Nationally Accredited and the go-to recognised qualification in industry.</p>
    <p>Did you know that Harlow has been operating in Australia for over 16 years! During this time, Harlow have developed a reputation second to none for training highly sought after medical receptionists, secretaries and administrators.</p>
    <p>Our course material and unique training programme is developed in conjunction with Industry to reflect the latest requirements in health administration. Harlow also believe understanding the medical culture is as important as good skills. Our team of specialised trainers are both experienced in industry and also hold special qualifications in adult education and are fully accredited.</p>
  </div>
</section>

<section class="courses">
  <h2 class="sec-title">List of Courses</h2>
  <div class="course-list">
    <div class="course"><div class="ico"><svg width="40" height="40" viewBox="0 0 40 40" fill="none" stroke="#fff" stroke-width="2.2"><rect x="14" y="4" width="12" height="6"/><path d="M12 10h16v26H12z"/><path d="M16 23h8M20 19v8"/></svg></div><h3>Medical Reception &amp; Terminology</h3></div>
    <div class="course"><div class="ico"><svg width="40" height="40" viewBox="0 0 40 40" fill="none" stroke="#fff" stroke-width="2.2"><circle cx="20" cy="9" r="5"/><path d="M13 36V20h14v16M20 20v16"/><path d="M6 26a14 14 0 0 1 6-10M34 26a14 14 0 0 0-6-10"/></svg></div><h3>Cert III Business Administration (Medical)</h3></div>
    <div class="course"><div class="ico"><svg width="40" height="40" viewBox="0 0 40 40" fill="none" stroke="#fff" stroke-width="2.2"><circle cx="20" cy="20" r="4"/><circle cx="20" cy="6" r="3"/><circle cx="33" cy="27" r="3"/><circle cx="7" cy="27" r="3"/><circle cx="32" cy="10" r="3"/><path d="M20 9v7M23.5 22l7 4M16.5 22l-7 4M23 17l7-5"/></svg></div><h3>Medical Terminology</h3></div>
    <div class="course"><div class="ico"><svg width="44" height="40" viewBox="0 0 44 40" fill="none" stroke="#fff" stroke-width="2.2"><rect x="4" y="14" width="36" height="18" rx="2"/><path d="M9 20h3M15 20h3M21 20h3M27 20h3M33 20h3M12 26h20M22 14V6"/></svg></div><h3>Keyboard and Typing</h3></div>
    <div class="course"><div class="ico"><svg width="40" height="40" viewBox="0 0 40 40" fill="none" stroke="#fff" stroke-width="2.2"><rect x="6" y="8" width="20" height="26" rx="2" transform="rotate(-10 16 21)"/><rect x="14" y="8" width="20" height="26" rx="2"/><circle cx="24" cy="18" r="3"/><path d="M19 28a5 5 0 0 1 10 0"/></svg></div><h3>Harlow Online</h3></div>
    <div class="course"><div class="ico"><svg width="40" height="40" viewBox="0 0 40 40" fill="none" stroke="#fff" stroke-width="2.2"><rect x="9" y="4" width="22" height="32" rx="2"/><rect x="14" y="10" width="12" height="8"/><path d="M14 23h12M14 28h12"/></svg></div><h3>Confidentiality</h3></div>
  </div>
</section>

<section class="enrol">
  <h2>Enrol in our new BSB51915 Diploma of Leadership and Management<br>and gain valuable skills to launch your managemnt career</h2>
  <a class="btn" href="#">Booking now!</a>
</section>

<section class="values">
  <div class="photo" role="img" aria-label="Photo of a softly lit hospital corridor"></div>
  <div class="shade"></div>
  <div class="value-list">
    <div class="value"><div class="ico"><svg width="40" height="40" viewBox="0 0 40 40" fill="none" stroke="#fff" stroke-width="2.4"><rect x="5" y="18" width="7" height="16"/><path d="M12 20l7-12c3 0 4 2 3 6l-1 4h10c2 0 3 2 2 4l-3 10c-1 2-2 2-4 2H12"/></svg></div><h3>Quality</h3><p>Harlow delivery quality, effective training facilitated by industry leaders. Just ask our students who rate us on average of 4.7 out of 5.</p></div>
    <div class="value"><div class="ico"><svg width="40" height="40" viewBox="0 0 40 40" fill="none" stroke="#fff" stroke-width="2.4"><path d="M34 6c-10 0-17 6-21 15l6 6c9-4 15-11 15-21z"/><circle cx="25" cy="15" r="2.5"/><path d="M13 21l-6 1 4-6h7M19 27l-1 6 6-4v-7M11 29l-4 4"/></svg></div><h3>Experience</h3><p>Harlow is Australia's largest and leading providers of nationally recognised training in health administration – training from over 17 locations Australia wide.</p></div>
    <div class="value active"><div class="ico"><span><svg width="36" height="30" viewBox="0 0 36 30" fill="none" stroke="#fff" stroke-width="2.2"><circle cx="13" cy="15" r="11"/><path d="M24 5a11 11 0 0 1 0 20M29 7a11 11 0 0 1 0 16"/><path d="M16 10h-4a2 2 0 0 0 0 5h2a2 2 0 0 1 0 5h-4M13 8v14"/></svg></span></div><h3>Value</h3><p>Our innovative teaching approach allows us to deliver exceptional training at affordable prices with no hidden extras.</p></div>
    <div class="value"><div class="ico"><svg width="42" height="40" viewBox="0 0 42 40" fill="none" stroke="#fff" stroke-width="2.4"><path d="M4 16l8-6 8 3 8-3 10 6-4 12-10 6-8-6-8-2z"/><path d="M20 13l-6 6 3 3 7-5M22 24l4 4M18 26l4 4"/></svg></div><h3>Industry Recognised</h3><p>Harlow work hand in hand with industry to develop our core programme and consolidate the programme annually to keep the programme fresh and relevant.</p></div>
    <div class="value"><div class="ico"><svg width="40" height="40" viewBox="0 0 40 40" fill="none" stroke="#fff" stroke-width="2.4"><path d="M12 6h16v10a8 8 0 0 1-16 0z"/><path d="M12 9H6c0 6 3 9 7 9M28 9h6c0 6-3 9-7 9M20 24v6M13 34h14"/></svg></div><h3>Great Job Results</h3><p>Harlow students get jobs! Our focus is to create job-ready students who are mentored to achieve their goals. Harlow also provide a recruitment service for industry and graduates.</p></div>
  </div>
</section>

<section class="reviews">
  <h2 class="sec-title">What People Say</h2>
  <div class="review-grid">
    <div class="review left"><blockquote>I want to say a huge thank you for the course and knowledge I came away with. I have secured a fantastic job after my first application! Such good value for money too! I would highly recommend it. I'm a mature age person so it's never too late to up-skill yourself to get what you deserve!<cite>Ruth Palmer</cite></blockquote><div class="avatar" role="img" aria-label="Portrait of Ruth Palmer" style="background:#c9ccd1"></div></div>
    <div class="review right"><div class="avatar" role="img" aria-label="Portrait of Tessa" style="background:#c8a991"></div><blockquote>"I have just completed my 6 month probation period at Bramwell Hospital and loving it. It was my first medical job I applied for literally 1-2 weeks after I finished the course. Thanks to you, Lina, and all the other teachers and staff at Harlow Health Management."<cite>Tessa</cite></blockquote></div>
    <div class="review left row2"><blockquote>I completed your Medical Receptionist course over a year ago. It was the best experience by far. I got a job 2 months after completing this course as a receptionist at a Neuro Physiotherapy practice. I have been with the practice little over a year and I am now the practice administrator. I love my job, I love the people I work with and I love going to work every day!<cite>Maree</cite></blockquote><div class="avatar" role="img" aria-label="Portrait of Maree" style="background:#b99a86"></div></div>
    <div class="review right row2"><div class="avatar" role="img" aria-label="Portrait of Dana" style="background:#a58a78"></div><blockquote>I started my working career in childcare. I always knew I am capable of more all I needed was the Harlow course – and to have faith in myself. My message to your future students is: believe in yourselves and everything will fall into place it doesn't matter if you're loud or quiet, shy or confident. I love my new position as a medical receptionist and I have never looked back!"<cite>Dana</cite></blockquote></div>
  </div>
</section>

<section class="posts">
  <h2 class="sec-title">Recent Posts</h2>
  <div class="post-list">
    <article class="post"><div class="thumb" role="img" aria-label="Photo of a traveller walking with a leather bag" style="background:linear-gradient(135deg,#5b4a3d,#a08466)"></div><div class="body"><h3>Standard Post</h3><p>Enim congue blandit. Lorem ipsum dolor sit amet, consectetur adipiscing elit. Quisque...</p><div class="meta"><span>▦ 22 June, 2015</span><span>▬ 0</span></div></div></article>
    <article class="post"><div class="thumb" role="img" aria-label="Dark video still" style="background:linear-gradient(135deg,#2d3640,#45505c)"><svg style="position:absolute;left:115px;top:88px" width="20" height="20" viewBox="0 0 20 20"><rect width="20" height="20" fill="#1a4fa3"/><path d="M8 6v8l6-4z" fill="#fff"/></svg></div><div class="body"><h3>Video Post</h3><p>Ultrices posuere cubilia curae curabitur sit amet tortor ut massa commodo. Vestibulum...</p><div class="meta"><span>▦ 22 June, 2015</span><span>▬ 0</span></div></div></article>
    <article class="post"><div class="thumb" role="img" aria-label="Photo of a café table against a brick wall" style="background:linear-gradient(135deg,#7a4a35,#c9a885)"></div><div class="body"><h3>Post with Image</h3><p>Enim congue blandit. Lorem ipsum dolor sit amet, consectetur adipiscing elit. Quisque...</p><div class="meta"><span>▦ 22 June, 2015</span><span>▬ 0</span></div></div></article>
    <article class="post"><div class="thumb" role="img" aria-label="Photo of a wallet and notes on a table" style="background:linear-gradient(135deg,#b7aa9a,#e2d9cc)"></div><div class="body"><h3>Image Post</h3><p>Ultrices posuere cubilia curae curabitur sit amet tortor ut massa commodo. Vestibulum...</p><div class="meta"><span>▦ 22 June, 2015</span><span>▬ 9</span></div></div></article>
  </div>
  <a class="more" href="#">VIEW MORE</a>
</section>

<footer class="footer">
  <div class="cols">
    <div class="col"><h4>About</h4><p>Maecenas etos sit amet, consectetur adipiscing elit. Terminal volutpat rutrum metro amet sollicitudin interdum. Maecenas etos sit amet, consectetur adipiscing elit. Terminal volutpat rutrum metro amet sollicitudin interdum. Maecenas etos sit amet, consectetur adipiscing elit. Terminal volutpat rutrum metro amet sollicitudin interdum.</p><div class="social"><i></i><i></i><i></i><i></i><i></i></div></div>
    <div class="col"><h4>Recent Posts</h4>
      <div class="mini"><span class="dot"></span><div><b>Business Cards Design Trends</b><small>Dec 02, 2020 / 2 comments</small></div></div>
      <div class="mini"><span class="dot"></span><div><b>This Maravelous App</b><small>Nov 18, 2020 / 9 comments</small></div></div>
      <div class="mini"><span class="dot"></span><div><b>Brand Paper Nicetiers</b><small>Nov 10, 2020 / 0 comments</small></div></div>
    </div>
    <div class="col"><h4>Latest Twitts</h4></div>
    <div class="col contact"><h4>Contact Us</h4><p>Maecenas etos sit amet, consectetur adipiscing elit. Terminal volutpat rutrum metro amet sollicitudin interdum.</p><p><strong>Phone:</strong> +1 (800) 555 01 23</p><p><strong>Office:</strong> 4410 Elm Row, Springfield</p><p><strong>Email:</strong> info@novella.example</p></div>
  </div>
  <div class="copyright">Copyright 2020. All Rights Reserved by Novella.</div>
</footer>

</body>
</html>
```